Vehicle graphics for healthcare company (bluecrestcare.co.uk)

I have a plain white van that needs some branding. I don't mind leaving a bit of the white, so I would consider a half wrap, or large panels of non-white, but I'm open to suggestion.

For a non-wrap design, I happened to see the KDO Van (attached photo), which I thought was a nice clear design. I thought maybe some elements of this could be included. Maybe their large A could be the S of my Blue Crest logo.

The only two colours the company has used to date are the green and grey of the logo. 1B7F8C and 58585A.

The core business we provide is assessment for people about to purchase a wheelchair. We take their measurements, look at their clinical needs and then recommend a product for them to purchase.

The information we need on it:
- our logo (attached)
- Private Wheelchair Assessment
- Occupational Therapy
- Wheelchair Skills

Our contact details to be included:
- www.bluecrestcare.co.uk
- info@bluecrestcare.co.uk
- 02937 418205

Target Market(s)

Wheelchair users and other healthcare providers.

Industry/Entity Type

Healthcare

Font styles to use
Other font styles liked:
• Arthaus Medium

Requirements
Must have
• Logo, contact details. Green/grey colours. 1B7F8C and 58585A
Nice to have
• See attached van, I thought this was a simple, clear design.
Should not have
• Clutter.

```html
<!DOCTYPE html>
<html lang="en">
<head>
<meta charset="utf-8">
<title>Blue Crest Therapy – Van Livery</title>
<link href="https://fonts.googleapis.com/css2?family=Ubuntu:wght@400;500;700&display=swap" rel="stylesheet">
<style>
  :root {
    --brand-teal: #1b7f8c;
    --brand-grey: #58585a;
    --panel-white: #ffffff;
    --backdrop: #ececec;
    --outline: #c9c9c9;
    --divider: #ffffff;
  }
  html, body {
    margin: 0;
    width: 1200px;
    height: 1200px;
    overflow: hidden;
    background: var(--backdrop);
    font-family: "Ubuntu", sans-serif;
  }
  .livery-sheet {
    width: 1200px;
    height: 1200px;
    display: flex;
    flex-direction: column;
  }
  .livery-variant {
    width: 1200px;
    height: 595px;
    display: block;
  }
  .sheet-divider {
    height: 10px;
    background: var(--divider);
  }
  .van-body { fill: var(--panel-white); stroke: var(--outline); stroke-width: 2; }
  .wrap-teal { fill: var(--brand-teal); }
  .wrap-grey { fill: var(--brand-grey); }
  .brand-name { fill: var(--brand-teal); font-weight: 500; }
  .brand-mark { fill: var(--brand-teal); }
  .contact-phone { fill: var(--brand-grey); font-weight: 700; font-size: 31px; }
  .contact-web { fill: var(--brand-teal); font-weight: 700; font-size: 16px; }
  .service-list { fill: var(--panel-white); font-weight: 700; font-size: 16px; }
  .service-dot { fill: var(--brand-teal); }
  .social-tile { fill: var(--brand-grey); }
</style>
</head>
<body>
<main class="livery-sheet">

  <!-- Variant A: with roof sweep -->
  <svg class="livery-variant" viewBox="0 0 1200 595" xmlns="http://www.w3.org/2000/svg">
    <defs>
      <clipPath id="body-a">
        <path d="M110,430 L100,340 Q110,300 200,268 L300,170 Q330,140 380,136 L1060,130 Q1088,132 1092,162 L1102,430 Q1102,450 1080,450 L1010,450 A95,95 0 0 0 830,450 L345,450 A95,95 0 0 0 160,450 L130,450 Q110,450 110,430 Z"/>
      </clipPath>
    </defs>
    <path class="van-body" d="M110,430 L100,340 Q110,300 200,268 L300,170 Q330,140 380,136 L1060,130 Q1088,132 1092,162 L1102,430 Q1102,450 1080,450 L1010,450 A95,95 0 0 0 830,450 L345,450 A95,95 0 0 0 160,450 L130,450 Q110,450 110,430 Z"/>
    <g clip-path="url(#body-a)">
      <polygon class="wrap-teal" points="240,180 300,130 880,130 430,160 330,210 290,280"/>
      <polygon class="wrap-grey" points="335,400 1100,290 1100,335 335,445"/>
      <polygon class="wrap-teal" points="335,452 1100,342 1100,460 335,460"/>
      <polygon class="wrap-teal" points="100,440 330,415 330,423 100,452"/>
      <polygon class="wrap-grey" points="100,455 330,430 330,436 100,462"/>
    </g>
    <circle class="brand-mark" cx="600" cy="245" r="30"/>
    <text class="brand-name" x="645" y="265" font-size="70">BLUE CREST</text>
    <text class="brand-name" x="660" y="318" font-size="40">THERAPY</text>
    <text class="contact-phone" x="305" y="320">02937 418205</text>
    <text class="contact-web" x="310" y="348">www.bluecrestcare.co.uk</text>
    <text class="contact-web" x="320" y="370">info@bluecrestcare.co.uk</text>
    <g class="service-band" transform="rotate(-8.2 800 355)">
      <circle class="service-dot" cx="674" cy="347" r="4"/>
      <text class="service-list" x="682" y="352">Occupational Therapy</text>
      <circle class="service-dot" cx="868" cy="347" r="4"/>
      <text class="service-list" x="876" y="352">Wheelchair Skills</text>
      <circle class="service-dot" cx="700" cy="367" r="4"/>
      <text class="service-list" x="708" y="372">Private Wheelchair Assessment</text>
    </g>
    <g class="social-icons">
      <rect class="social-tile" x="1068" y="362" width="15" height="15"/>
      <rect class="social-tile" x="1068" y="382" width="15" height="15"/>
      <rect class="social-tile" x="1068" y="402" width="15" height="15"/>
      <rect class="social-tile" x="1068" y="422" width="15" height="15"/>
    </g>
  </svg>

  <div class="sheet-divider"></div>

  <!-- Variant B: white roof -->
  <svg class="livery-variant" viewBox="0 0 1200 595" xmlns="http://www.w3.org/2000/svg">
    <defs>
      <clipPath id="body-b">
        <path d="M110,430 L100,340 Q110,300 200,268 L300,170 Q330,140 380,136 L1060,130 Q1088,132 1092,162 L1102,430 Q1102,450 1080,450 L1010,450 A95,95 0 0 0 830,450 L345,450 A95,95 0 0 0 160,450 L130,450 Q110,450 110,430 Z"/>
      </clipPath>
    </defs>
    <path class="van-body" d="M110,430 L100,340 Q110,300 200,268 L300,170 Q330,140 380,136 L1060,130 Q1088,132 1092,162 L1102,430 Q1102,450 1080,450 L1010,450 A95,95 0 0 0 830,450 L345,450 A95,95 0 0 0 160,450 L130,450 Q110,450 110,430 Z"/>
    <g clip-path="url(#body-b)">
      <polygon class="wrap-grey" points="335,400 1100,290 1100,335 335,445"/>
      <polygon class="wrap-teal" points="335,452 1100,342 1100,460 335,460"/>
      <polygon class="wrap-teal" points="100,440 330,415 330,423 100,452"/>
      <polygon class="wrap-grey" points="100,455 330,430 330,436 100,462"/>
    </g>
    <circle class="brand-mark" cx="600" cy="245" r="30"/>
    <text class="brand-name" x="645" y="265" font-size="70">BLUE CREST</text>
    <text class="brand-name" x="660" y="318" font-size="40">THERAPY</text>
    <text class="contact-phone" x="305" y="320">02937 418205</text>
    <text class="contact-web" x="310" y="348">www.bluecrestcare.co.uk</text>
    <text class="contact-web" x="320" y="370">info@bluecrestcare.co.uk</text>
    <g class="service-band" transform="rotate(-8.2 800 355)">
      <circle class="service-dot" cx="674" cy="347" r="4"/>
      <text class="service-list" x="682" y="352">Occupational Therapy</text>
      <circle class="service-dot" cx="868" cy="347" r="4"/>
      <text class="service-list" x="876" y="352">Wheelchair Skills</text>
      <circle class="service-dot" cx="700" cy="367" r="4"/>
      <text class="service-list" x="708" y="372">Private Wheelchair Assessment</text>
    </g>
    <g class="social-icons">
      <rect class="social-tile" x="1068" y="362" width="15" height="15"/>
      <rect class="social-tile" x="1068" y="382" width="15" height="15"/>
      <rect class="social-tile" x="1068" y="402" width="15" height="15"/>
      <rect class="social-tile" x="1068" y="422" width="15" height="15"/>
    </g>
  </svg>

</main>
</body>
</html>
```